Brookvane Eyecare Optometrists

News paper advertisement (150mm H x 110mm W).
Eye testing (Tallacor covered).
Prescription glasses,sunglasses & contact lenses.
All major health funds accepted.
Phone: 94517038 for an appointment at our Kellsburn practice
or Phone: 95643218 for an appointment at our Meridon practice.
Please disregard "Good health for less" slogan.
We are an independent Optometry practice providing major fashion brands in both Optical frames & sunglasses.
Keep it simple and / or entertaining.
Use of company logo not critical, only discretionary.
Use as much or as little of this information as you wish.

```html
<!DOCTYPE html>
<html lang="en">
<head>
<meta charset="utf-8">
<title>Brookvane Eyecare Optometrists – Eye Testing</title>
<link rel="stylesheet" href="https://fonts.googleapis.com/css2?family=Arimo:wght@400;700&display=swap">
<style>
  :root {
    --ink: #1d1d1b;
    --paper: #ffffff;
    --mist-top: #dadada;
    --mist-bottom: #f5f5f5;
    --frame-tone: #4a5a44;
    --signal-red: #e41e26;
    --sun-yellow: #ffe600;
  }
  * { margin: 0; padding: 0; box-sizing: border-box; }
  html, body { width: 879px; height: 1200px; overflow: hidden; background: var(--paper); }
  .ad {
    position: relative;
    width: 879px;
    height: 1200px;
    overflow: hidden;
    background: var(--paper);
    font-family: "Arimo", Arial, sans-serif;
    color: var(--ink);
  }
  .headline-block {
    position: absolute;
    top: 0; left: 0;
    width: 100%;
    height: 532px;
    text-align: center;
  }
  .headline {
    position: absolute; left: 0; width: 100%;
    top: 116px;
    font-size: 64px; font-weight: 700;
    letter-spacing: 0.06em;
  }
  .coverage {
    position: absolute; left: 0; width: 100%;
    top: 214px;
    font-size: 33px; font-weight: 700;
    letter-spacing: 0.09em;
  }
  .prescription {
    position: absolute; left: 0; width: 100%;
    top: 279px;
    font-size: 33px; font-weight: 700;
    letter-spacing: 0.32em;
    padding-left: 0.32em;
  }
  .range {
    position: absolute; left: 0; width: 100%;
    top: 351px;
    font-size: 14px; font-weight: 700;
  }
  .funds {
    position: absolute; left: 0; width: 100%;
    top: 404px;
    font-size: 14px; font-weight: 700;
  }
  .showcase {
    position: absolute;
    top: 532px; left: 0;
    width: 100%; height: 480px;
    background: linear-gradient(to bottom, var(--mist-top), var(--mist-bottom));
  }
  .frames-visual {
    position: absolute;
    left: 255px; top: 98px;
    width: 366px; height: 106px;
    border-radius: 20px;
    background: radial-gradient(ellipse at center, #e6e9e2 0%, #b9c2b2 60%, var(--frame-tone) 100%);
    opacity: 0.85;
  }
  .contact-band {
    position: absolute;
    left: 0; top: 900px;
    width: 879px; height: 300px;
  }
  .call-now {
    position: absolute;
    left: 22px; top: 1004px;
    font-size: 33px; font-weight: 700;
    color: var(--paper);
    letter-spacing: 0.08em;
    transform: rotate(-8deg);
    transform-origin: left bottom;
  }
  .phone-line {
    position: absolute;
    left: 240px;
  }
  .phone-line.kellsburn { top: 988px; }
  .phone-line.meridon { top: 1088px; }
  .phone-number {
    display: block;
    font-size: 57px; font-weight: 700;
    line-height: 1;
    color: var(--sun-yellow);
    letter-spacing: -0.01em;
  }
  .practice-note {
    display: block;
    margin-top: 4px;
    font-size: 22px; font-weight: 700;
    color: var(--paper);
  }
  .brand-mark {
    position: absolute;
    left: 38px; top: 1080px;
    width: 150px; height: 98px;
    display: flex; align-items: center; gap: 8px;
  }
  .brand-square {
    width: 18px; height: 18px;
    background: var(--sun-yellow);
    flex: none;
  }
  .brand-name {
    font-size: 21px; font-weight: 700;
    line-height: 1.1;
    color: var(--paper);
  }
</style>
</head>
<body>
<main class="ad">
  <section class="headline-block">
    <h1 class="headline">EYE TESTING</h1>
    <p class="coverage">TALLACOR COVERED</p>
    <p class="prescription">PRESCRIPTION</p>
    <p class="range">GLASSES,SUNGLASSES &amp; CONTACT LENSES</p>
    <p class="funds">ALL MAJOR HEALTH FUNDS ACCEPTED</p>
  </section>

  <section class="showcase">
    <div class="frames-visual" role="img" aria-label="Photograph of a pair of green rectangular prescription eyeglass frames"></div>
  </section>

  <svg class="contact-band" viewBox="0 0 879 300" aria-hidden="true">
    <path d="M0 78 Q440 8 879 66 L879 300 L0 300 Z" fill="var(--sun-yellow)"/>
    <path d="M0 88 Q440 18 879 76 L879 300 L0 300 Z" fill="var(--signal-red)"/>
  </svg>

  <p class="call-now">CALL NOW</p>

  <p class="phone-line kellsburn">
    <span class="phone-number">94517038</span>
    <span class="practice-note">FOR AN APPOINTMENT AT OUR KELLSBURN PRACTICE</span>
  </p>
  <p class="phone-line meridon">
    <span class="phone-number">95643218</span>
    <span class="practice-note">FOR AN APPOINTMENT AT OUR MERIDON PRACTICE</span>
  </p>

  <div class="brand-mark">
    <span class="brand-square"></span>
    <span class="brand-name">Brookvane<br>Eyecare</span>
  </div>
</main>
</body>
</html>
```